Luxury Skincare Product Box Packaging Design

Vorastelle is a range of skincare products that help protect, nourish, and strengthen even the most sensitive skin, ensuring it is healthy, glowing, calm, and soft. Skincare practices support skin to enhance its appearance and relieve skin conditions. Your skin reflects your health. It is your body canvas and is an asset. The products contain naturally derived ingredients, aromatherapy oils, sustainable and ethical ingredients, organic ingredients where possible, natural preservatives and Australian oils, fruits, and extracts.

Vorastelle
Tagline is "Where Calm Finds Bloom"

Our products do not contain sulphates, parabens, phthalates, petrochemicals, synthetic colours, nor synthetic fragrances.

Everything about the Vorastelle Skincare name is creative and communicates luxury. Vorastelle from your first glance of the name, you will know that this is a company with excellent products.

By keeping it simple, unique, and elegant is often associated with high quality and is a way to establish trust. Vorastelle is a product that is “pure” and natural, so Vorastelle packaging would look simple, elegant, and clean.

I have uploaded the actual logo design and individual labels for the current skincare range I currently with the ingredients included so you can get an understanding of what I like. I have also added samples of package designs I quite like to assist with your designs.

Each Product box packaging sizes are as follows:

Product One - Exfoliating Herbs: 110mm (H) x 33mm Diameter
Product Two - Probiotic Lotion: 138mm (H) x 33mm Diameter
Product Three - Vitamin A Serum: 120mm (H) x 30mm Diameter
Updates

The Measurements are as follows: Product One: 110mm (H) x 33mm Diameter Product Two: 138mm (H) x 33mm Diameter Product Three: 120mm (H) x 30mm Diameter

Target Market(s)

Women

Requirements
Must have
• Logo, Product Name and ingredients and if you can barcode on the packaging that is the box design I am after
Nice to have
• samples of designs I like but open to suggestions

```html
<!DOCTYPE html>
<html lang="en">
<head>
<meta charset="utf-8">
<title>Vorastelle – Gentle Exfoliating Herbs Box Dieline</title>
<link rel="stylesheet" href="https://fonts.googleapis.com/css2?family=Montserrat:wght@300;400;600;700&display=swap">
<style>
  :root{
    --paper:#ffffff;
    --mist:#f3faf6;
    --mint:#a9dcc4;
    --mint-deep:#8fd0b2;
    --cut:#e8505b;
    --ink:#111111;
    --ink-soft:#2b2b2b;
    --tagline:#6f7a76;
    --copper:#b57d62;
    --copper-light:#e7b7a2;
    --copper-dark:#8c5a45;
  }
  *{box-sizing:border-box;margin:0;padding:0}
  html,body{width:1200px;height:1200px;overflow:hidden;background:var(--paper)}
  .canvas{position:relative;width:1200px;height:1200px;font-family:'Montserrat',sans-serif;color:var(--ink)}
  .dieline{position:absolute;inset:0}
  .panel-text{position:absolute;text-align:center}

  .back-copy{left:272px;top:326px;width:154px;font-size:10px;line-height:12.8px;font-weight:300;color:var(--ink-soft)}
  .back-copy p{margin-bottom:12.8px}
  .back-copy strong{font-weight:600;color:var(--ink)}
  .back-copy .ingredients{text-transform:uppercase;margin-bottom:0}

  .caution{position:absolute;left:277px;top:694px;width:144px;height:87px;border:2px solid var(--ink);
    display:flex;align-items:center;justify-content:center;text-align:center;
    font-size:8.6px;line-height:14px;font-weight:600;color:var(--ink);padding:0 6px}

  .badges{position:absolute;left:274px;top:804px;width:150px;display:flex;justify-content:space-between}
  .badge{width:28px;display:flex;flex-direction:column;align-items:center}
  .badge-mark{width:22px;height:22px;border-radius:50%;border:1.6px solid #1e6b2c}
  .badge-label{font-size:4.4px;line-height:5px;font-weight:600;color:var(--ink);margin-top:2px;text-align:center;white-space:nowrap}

  .website{left:257px;top:874px;width:184px;font-size:10px;font-weight:600;color:var(--ink)}

  .tagline-stack{position:absolute;width:184px;top:0;height:1200px}
  .tagline-stack span{position:absolute;left:0;width:100%;text-align:center;font-size:8.8px;letter-spacing:3px;color:var(--tagline);font-weight:400}
  .side-a{left:441px}
  .side-b{left:810px}

  .brand-name{position:absolute;left:700px;top:500px;transform:translate(-50%,-50%) rotate(-90deg);
    font-size:46px;font-weight:300;letter-spacing:3px;color:var(--copper);white-space:nowrap}

  .product-name{position:absolute;left:646px;top:667px;font-size:23px;line-height:26.5px;font-weight:300;letter-spacing:.5px;color:var(--ink)}
  .skin-chip{position:absolute;left:646px;top:755px;width:120px;height:19px;
    background:linear-gradient(90deg,var(--copper-light),var(--copper) 55%,var(--copper-dark));
    color:#fff;font-size:12.4px;font-weight:300;line-height:19px;text-align:center;letter-spacing:.2px}
  .volume{position:absolute;left:646px;top:881px;font-size:10px;font-weight:400;color:var(--ink)}
</style>
</head>
<body>
<main class="canvas">
  <svg class="dieline" width="1200" height="1200" viewBox="0 0 1200 1200">
    <defs>
      <clipPath id="box-shape">
        <path d="M257 296 L212.5 319 V888 L257 911 Z"/>
        <rect x="257" y="296" width="737" height="615"/>
        <path d="M626 296 V100 Q626 44 682 44 H754 Q810 44 810 100 V296 Z"/>
        <path d="M441 296 V275 L455 266 L477 211 H589 L616 287 L626 296 Z"/>
        <path d="M810 296 L819 287 L846 211 H958 L982 266 L994 275 V296 Z"/>
        <path d="M441 911 L450 918 L477 996 H589 L612 938 L626 930 V911 Z"/>
        <path d="M810 911 V930 L824 938 L847 996 H959 L986 918 L994 911 Z"/>
        <path d="M257 911 V1106 Q257 1162 313 1162 H385 Q441 1162 441 1106 V911 Z"/>
      </clipPath>
      <radialGradient id="wash" cx="50%" cy="50%" r="50%">
        <stop offset="0" stop-color="var(--mint-deep)" stop-opacity=".75"/>
        <stop offset=".55" stop-color="var(--mint)" stop-opacity=".45"/>
        <stop offset="1" stop-color="var(--mint)" stop-opacity="0"/>
      </radialGradient>
    </defs>

    <g clip-path="url(#box-shape)">
      <rect width="1200" height="1200" fill="var(--mist)"/>
      <g role="img" aria-label="Soft mint watercolour wash with faint outlined flowers">
        <ellipse cx="718" cy="140" rx="160" ry="170" fill="url(#wash)"/>
        <ellipse cx="535" cy="250" rx="120" ry="80" fill="url(#wash)"/>
        <ellipse cx="905" cy="250" rx="120" ry="80" fill="url(#wash)"/>
        <ellipse cx="520" cy="520" rx="150" ry="210" fill="url(#wash)"/>
        <ellipse cx="440" cy="600" rx="90" ry="200" fill="url(#wash)"/>
        <ellipse cx="760" cy="620" rx="120" ry="160" fill="url(#wash)"/>
        <ellipse cx="930" cy="640" rx="150" ry="220" fill="url(#wash)"/>
        <ellipse cx="230" cy="780" rx="60" ry="140" fill="url(#wash)"/>
        <ellipse cx="530" cy="950" rx="110" ry="70" fill="url(#wash)"/>
        <ellipse cx="330" cy="925" rx="110" ry="40" fill="url(#wash)"/>
        <ellipse cx="860" cy="930" rx="90" ry="40" fill="url(#wash)"/>
      </g>
    </g>

    <g fill="none" stroke="var(--cut)" stroke-width=".8">
      <path d="M257 296 L212.5 319 V888 L257 911"/>
      <rect x="257" y="296" width="737" height="615"/>
      <line x1="441" y1="296" x2="441" y2="911"/>
      <line x1="626" y1="296" x2="626" y2="911"/>
      <line x1="810" y1="296" x2="810" y2="911"/>
      <path d="M626 296 V100 Q626 44 682 44 H754 Q810 44 810 100 V296"/>
      <line x1="626" y1="111" x2="810" y2="111"/>
      <path d="M441 296 V275 L455 266 L477 211 H589 L616 287 L626 296"/>
      <path d="M810 296 L819 287 L846 211 H958 L982 266 L994 275 V296"/>
      <path d="M441 911 L450 918 L477 996 H589 L612 938 L626 930 V911"/>
      <path d="M810 911 V930 L824 938 L847 996 H959 L986 918 L994 911"/>
      <path d="M257 911 V1106 Q257 1162 313 1162 H385 Q441 1162 441 1106 V911"/>
      <line x1="257" y1="1095" x2="441" y2="1095"/>
    </g>
  </svg>

  <section class="panel-text back-copy">
    <p><strong>All Skin Types</strong><br>Particularly beneficial for sensitive, stressed and delicate skins</p>
    <p><strong>Direction:</strong> Mic a small amount with your favourite cleanser. Massage into your face for approximately one minute before removing with water or a face cloth. Use twice weekly.</p>
    <p class="ingredients"><strong>Ingredients:</strong> Oryza sativa (rice) powder*, rosa gallica (rose petals)*, jasminum officinale (jasmine) flower, matricaria recutita (chamomile flowers)*, camellia sinensis leaf (green tea), luffa cylindrica fruit powder, calendula officinalis (marigold flowers)<br><strong>*Organic ingredients</strong></p>
  </section>

  <div class="caution">Store in a cool dry place Caution For external use only. Avoid contact with eyes. If irritation occurs, discontinue use.</div>

  <ul class="badges">
    <li class="badge"><span class="badge-mark"></span><span class="badge-label">Australian<br>Made</span></li>
    <li class="badge"><span class="badge-mark"></span><span class="badge-label">100%<br>Vegan</span></li>
    <li class="badge"><span class="badge-mark"></span><span class="badge-label">Cruelty<br>Free</span></li>
    <li class="badge"><span class="badge-mark"></span><span class="badge-label">Please<br>Recycle</span></li>
    <li class="badge"><span class="badge-mark"></span><span class="badge-label">6 months<br>once open</span></li>
  </ul>

  <p class="panel-text website">www.vorastelle.com</p>

  <div class="tagline-stack side-a">
    <span style="top:420px">Where</span><span style="top:538px">Calm</span><span style="top:656px">Finds</span><span style="top:774px">Bloom</span>
  </div>
  <div class="tagline-stack side-b">
    <span style="top:420px">Where</span><span style="top:538px">Calm</span><span style="top:656px">Finds</span><span style="top:774px">Bloom</span>
  </div>

  <h1 class="brand-name">Vorastelle</h1>
  <h2 class="product-name">GENTLE<br>EXFOLIATING<br>HERBS</h2>
  <p class="skin-chip">ALL SKIN TYPES</p>
  <p class="volume">40 ml</p>
</main>
</body>
</html>
```